Stanbrook Fire Services Pty Ltd

We need business cards for a company based in Perth, we install, service and maintain fire equipment.
On the front we want a great design with our logo and a small spot for our full company name, general company email address and office number. On the back we need space for our name, title, mobile number and email address on the back.

Target Market(s)

Facility managers and commercial/industrial building owners/occupiers.

Contact Information for Business Card

Font styles to use
Sans Serif

Requirements
Must have
• Please only submit 5 of your best samples.
Darker tones are preferred.
Nice to have
• We want to use, black, red and grey. Keep it modern and clean.
I've attached the company logo and a sample of a boarder we use on our emergency plans.
Should not have
• No preference. Let the designer choose.

```html
<!DOCTYPE html>
<html lang="en">
<head>
<meta charset="utf-8">
<title>Stanbrook Fire Services – Business Cards</title>
<link rel="stylesheet" href="https://fonts.googleapis.com/css2?family=Montserrat:wght@700&family=Roboto:wght@400&display=swap">
<style>
  :root {
    --stage: #141414;
    --card: #1d1d1f;
    --red: #e5242b;
    --grey: #8a8a8e;
    --rule: #55555a;
    --white: #f2f2f2;
  }
  * { box-sizing: border-box; margin: 0; padding: 0; }
  html, body { width: 1200px; height: 900px; overflow: hidden; }
  body {
    background: var(--stage);
    position: relative;
    font-family: "Roboto", Arial, sans-serif;
  }
  .card {
    position: absolute;
    left: 250px;
    width: 700px;
    height: 400px;
    background: var(--card);
    box-shadow: 0 12px 30px rgba(0,0,0,.6);
  }
  .card--front { top: 40px; }
  .card--back { top: 470px; }

  .wordmark {
    position: absolute;
    left: 50px;
    top: 60px;
    display: flex;
    align-items: center;
    gap: 14px;
    font-family: "Montserrat", Arial, sans-serif;
    font-weight: 700;
    letter-spacing: 2px;
  }
  .wordmark__square { width: 26px; height: 26px; }
  .card--front .wordmark { color: var(--grey); font-size: 46px; }
  .card--front .wordmark__square { background: var(--grey); }
  .card--back .wordmark { color: var(--red); font-size: 54px; }
  .card--back .wordmark__square { background: var(--red); width: 30px; height: 30px; }

  .company-name, .person-name {
    position: absolute;
    left: 50px;
    font-family: "Montserrat", Arial, sans-serif;
    font-weight: 700;
    color: var(--red);
    text-transform: uppercase;
  }
  .company-name { top: 200px; font-size: 19px; letter-spacing: .5px; }
  .person-name { top: 186px; font-size: 30px; letter-spacing: 1px; }
  .person-title {
    position: absolute;
    left: 50px;
    top: 226px;
    font-size: 18px;
    color: var(--white);
  }

  .divider {
    position: absolute;
    left: 50px;
    right: 0;
    top: 262px;
    height: 1px;
    background: var(--rule);
  }
  .divider__accent {
    position: absolute;
    right: 0;
    top: -3px;
    width: 70px;
    height: 6px;
    background: var(--red);
  }

  .contact-list {
    position: absolute;
    left: 50px;
    top: 286px;
    list-style: none;
    color: var(--white);
  }
  .contact-list li {
    display: flex;
    align-items: center;
    gap: 12px;
    height: 32px;
  }
  .contact-list .phone { font-size: 22px; }
  .contact-list .email { font-size: 18px; }
  .contact-list svg { width: 18px; height: 18px; fill: var(--red); flex: none; }
</style>
</head>
<body>

<section class="card card--front" aria-label="Card front">
  <div class="wordmark"><span class="wordmark__square"></span>STANBROOK</div>
  <p class="company-name">Stanbrook Fire Services Pty Ltd</p>
  <div class="divider"><span class="divider__accent"></span></div>
  <ul class="contact-list">
    <li class="phone">
      <svg viewBox="0 0 24 24" aria-hidden="true"><path d="M6.6 10.8a15 15 0 0 0 6.6 6.6l2.2-2.2c.3-.3.7-.4 1-.2 1.1.4 2.3.6 3.6.6.6 0 1 .4 1 1V20c0 .6-.4 1-1 1A17 17 0 0 1 3 4c0-.6.4-1 1-1h3.5c.6 0 1 .4 1 1 0 1.3.2 2.5.6 3.6.1.3 0 .7-.2 1z"/></svg>
      108 555 0142
    </li>
    <li class="email">
      <svg viewBox="0 0 24 24" aria-hidden="true"><path d="M2 5h20v14H2zm2 2v.5l8 5 8-5V7l-8 5z"/></svg>
      office@stanbrookfire.au
    </li>
  </ul>
</section>

<section class="card card--back" aria-label="Card back">
  <div class="wordmark"><span class="wordmark__square"></span>STANBROOK</div>
  <p class="person-name">Daniel Hartley</p>
  <p class="person-title">Owner/ CEO</p>
  <div class="divider"><span class="divider__accent"></span></div>
  <ul class="contact-list">
    <li class="phone">
      <svg viewBox="0 0 24 24" aria-hidden="true"><path d="M7 2h10a2 2 0 0 1 2 2v16a2 2 0 0 1-2 2H7a2 2 0 0 1-2-2V4a2 2 0 0 1 2-2zm0 3v13h10V5zm4 14.2h2v1.3h-2z"/></svg>
      108 555 0142
    </li>
    <li class="email">
      <svg viewBox="0 0 24 24" aria-hidden="true"><path d="M2 5h20v14H2zm2 2v.5l8 5 8-5V7l-8 5z"/></svg>
      daniel@stanbrookfire.au
    </li>
  </ul>
</section>

</body>
</html>
```